Postcard Design

I am a practicing Obstetrician and Gynecologist. I am working at a clinic called Corvane Ridge Health System. I am looking for a design of a personal advertisement card that can be mailed, handed out, or sent an an electronic copy to the local newspaper to be placed as an ad. I previously worked for another clinic called TBW. They had an ad on my I liked very much, but I cannot use it. It is proprietary to them. I would like something like it. Copy attached. I want my foto and text. I have Printhollow Business Cards with Corvane Ridge and Stationary already. Access permitted. I would like to stay within that light blue - light green color scheme. I want the card to have me come across as competent and knowledgeable, but also as gentle, compassionate, benevolent, caring, knowledgeable, competent. Obviously, it has to appeal to women.

Target Market(s)

Public, patients, women

Industry/Entity Type

Electronic

Requirements
Nice to have
• A sophisticated, tasteful and inspiring maternity care image is very hard to find. I love the one on my business card. If it or something like it could be found and incorporated, that would be nice. I like a warm, soft, friendly font, Calibri light italic, Archer, Gotham. Describes nicely:Archer, the colorful slab serif. Sweet but not saccharine, earnest but not grave, Archer is designed to hit just the right notes of forthrightness, credibility, and charm.

```html
<!DOCTYPE html>
<html lang="en">
<head>
<meta charset="utf-8">
<title>Dr. Konrad E. Wallner – Obstetrician &amp; Gynecologist</title>
<link href="https://fonts.googleapis.com/css2?family=Jost:ital,wght@0,400;0,500;0,700;1,400;1,700&display=swap" rel="stylesheet">
<style>
  :root {
    --ink: #141414;
    --panel: rgba(255,255,255,0.93);
    --sky-top: #dfe6e4;
    --sky-warm: #f3e6c8;
    --sky-haze: #e8eddc;
    --meadow-light: #cfe07a;
    --meadow: #9cc24a;
    --meadow-deep: #6f9a2e;
    --coat: #f4f4f2;
    --coat-shade: #dcdcd8;
    --band: rgba(255,255,255,0.85);
  }
  html, body { margin: 0; padding: 0; overflow: hidden; }
  body { width: 1200px; height: 926px; font-family: "Jost", "Century Gothic", sans-serif; color: var(--ink); }
  .card {
    position: relative; width: 1200px; height: 926px; overflow: hidden;
    background: linear-gradient(180deg, var(--sky-top) 0%, var(--sky-warm) 22%, var(--sky-haze) 42%, var(--meadow-light) 68%, var(--meadow) 85%, var(--meadow-deep) 100%);
  }
  .portrait {
    position: absolute; left: 640px; top: 0; width: 560px; height: 836px;
    background:
      radial-gradient(ellipse 120px 150px at 315px 230px, #d9b8a4 0%, #c89c86 70%, transparent 72%),
      radial-gradient(ellipse 260px 420px at 330px 700px, var(--coat) 0%, var(--coat-shade) 80%, transparent 82%);
  }
  .info-panel {
    position: absolute; left: 34px; top: 50px; width: 662px; height: 718px;
    background: var(--panel);
  }
  .doctor-name {
    position: absolute; left: 0; width: 662px; top: 34px; margin: 0;
    text-align: center; font-weight: 700; font-size: 34px; line-height: 44px; letter-spacing: 0.4px;
  }
  .doctor-name em { font-style: italic; }
  .credentials { position: absolute; left: 0; width: 662px; top: 82px; margin: 0; text-align: center; font-size: 32px; line-height: 44px; font-weight: 400; }
  .specialty { position: absolute; left: 0; width: 662px; top: 123px; margin: 0; text-align: center; font-size: 21px; line-height: 30px; letter-spacing: 0.4px; }
  .text { position: absolute; left: 28px; width: 608px; font-size: 19.6px; line-height: 28.6px; letter-spacing: 0.7px; margin: 0; }
  .bio { top: 172px; text-align: justify; text-align-last: left; }
  .training { top: 314px; }
  .focus { top: 487px; text-align: justify; }
  .label { font-weight: 700; }
  .contact { position: absolute; top: 574px; font-size: 19.6px; line-height: 28.6px; letter-spacing: 0.5px; margin: 0; }
  .contact.address { left: 28px; }
  .contact.booking { left: 324px; }
  .phone { font-weight: 700; letter-spacing: 0.8px; }
  .insurance-band {
    position: absolute; left: 0; top: 836px; width: 1200px; height: 80px; background: var(--band);
  }
  .insurance-band p {
    margin: 0; position: absolute; left: 38px; top: 12px; width: 1150px;
    font-style: italic; font-size: 18px; line-height: 27px; letter-spacing: 0.2px;
  }
  .base-strip { position: absolute; left: 0; top: 916px; width: 1200px; height: 10px; background: var(--meadow-deep); }
</style>
</head>
<body>
  <div class="card">
    <div class="portrait" role="img" aria-label="Portrait photo of the doctor in a white coat, arms crossed, smiling"></div>

    <section class="info-panel">
      <h1 class="doctor-name">KONRAD E. <em>(“ KEN ”)</em> WALLNER</h1>
      <p class="credentials">MD, FACOG</p>
      <p class="specialty">BOARD CERTIFIED OBSTETRICIAN &amp; GYNECOLOGIST</p>

      <p class="text bio"><span class="label">Dr. Wallner</span> is a Board Certified OB/GYN and was in private practice in Atlanta, Georgia for twenty-five years. He recently was the in-house hospitalist Obstetrics and Gynecology at the Harbor Memorial Hospital.</p>

      <p class="text training">
        <span class="label">Education:</span><br>
        Elbmark University School of Medicine, Germany<br>
        <span class="label">Residency and Internship:</span><br>
        Eastbridge University School of Medicine, New York<br>
        <span class="label">Residency:</span> Ohio Valley University School of Medicine, Kentucky
      </p>

      <p class="text focus">Dr. Wallner specializes in preventive medicine and women’s well-ness and weight management</p>

      <p class="contact address">
        <span class="label">Accepting New Patients at</span><br>
        Corvane Ridge Health System<br>
        214-B Marisol Avenue<br>
        Port Arden, GU 96920
      </p>
      <p class="contact booking">
        Please call for an appointment at<br>
        <span class="phone">671-555-0142</span><br>
        <br>
        Fax: 671-555-0187
      </p>
    </section>

    <div class="insurance-band">
      <p>CREDENTIALED PROVIDER WITH NORTHSTAR GLOBAL, AZURE SHIELD HEALTH, MARIN’S CHOICECARE, MEDICAID, MEDICARE, IHP, LINKCARE, KEEPWELL, HOLDCARE, TRISERVE.&nbsp; REFERRAL REQUIRED WITH SOME PLANS.</p>
    </div>
    <div class="base-strip"></div>
  </div>
</body>
</html>
```